Business cards and stationary
Pepa Ruvel's Charred Relish
Bright & Fun-filled
Howard Pellingham
P. O Box 7413
Alder Point, CA, 90417
855-PEPA-RUV (855-737-2788)
howard@CharredRelish.com
www.CharredRelish.com
I will upload my logo in AI format. Please choose the color scheme accordingly.
Salsa. It's not just for chips anymore!

```html
<!DOCTYPE html>
<html lang="en">
<head>
<meta charset="utf-8">
<title>Pepa Ruvel's Charred Relish – Business Card</title>
<link rel="stylesheet" href="https://fonts.googleapis.com/css2?family=Source+Sans+3:wght@400;600;700&display=swap">
<style>
  :root {
    --backdrop: #e9e6e2;
    --card: #ffffff;
    --salsa-red: #e0212a;
    --deep-red: #b5141c;
    --chili-green: #1f9a3e;
    --ink: #4a4a4a;
    --rule: #b9b9b9;
    --shadow: rgba(0, 0, 0, 0.22);
  }
  * { box-sizing: border-box; margin: 0; padding: 0; }
  html, body {
    width: 1200px;
    height: 780px;
    overflow: hidden;
    background: var(--backdrop);
    font-family: "Source Sans 3", Arial, sans-serif;
  }
  .business-card {
    position: absolute;
    left: 80px;
    top: 93px;
    width: 1040px;
    height: 594px;
    background: var(--card);
    border-radius: 34px;
    overflow: hidden;
    box-shadow: 0 14px 34px var(--shadow);
  }
  .header-band {
    position: absolute;
    inset: 0 0 auto 0;
    width: 1040px;
    height: 240px;
  }
  .holder-name {
    position: absolute;
    right: 52px;
    top: 58px;
    color: #fff;
    font-weight: 700;
    font-size: 38px;
    letter-spacing: 0.2px;
  }
  .brand-mark {
    position: absolute;
    left: 70px;
    top: 312px;
    width: 380px;
    display: flex;
    align-items: center;
    gap: 18px;
  }
  .brand-square {
    flex: none;
    width: 44px;
    height: 44px;
    background: var(--chili-green);
  }
  .brand-name {
    color: var(--salsa-red);
    font-weight: 700;
    font-size: 38px;
    line-height: 1.08;
  }
  .divider {
    position: absolute;
    left: 486px;
    top: 250px;
    width: 2px;
    height: 272px;
    background: var(--rule);
  }
  .contact-block {
    position: absolute;
    left: 516px;
    top: 248px;
    color: var(--ink);
    font-size: 27px;
    line-height: 1.25;
  }
  .address { margin-bottom: 26px; }
  .contact-list { list-style: none; }
  .contact-list li {
    display: flex;
    align-items: center;
    gap: 12px;
    height: 40px;
  }
  .contact-icon { width: 24px; height: 24px; flex: none; }
</style>
</head>
<body>
  <article class="business-card">
    <svg class="header-band" viewBox="0 0 1040 240" aria-hidden="true">
      <path d="M0 0 H1040 V150 C820 138 560 142 360 168 C220 186 100 200 0 196 Z" fill="var(--salsa-red)"/>
      <path d="M0 196 C100 200 220 186 360 168 C560 142 820 138 1040 150 V176 C820 156 560 162 360 184 C220 200 100 210 0 204 Z" fill="var(--chili-green)"/>
    </svg>
    <h1 class="holder-name">Howard Pellingham</h1>

    <div class="brand-mark">
      <span class="brand-square"></span>
      <span class="brand-name">Pepa Ruvel's Charred Relish</span>
    </div>

    <div class="divider"></div>

    <div class="contact-block">
      <p class="address">P. O Box 7413<br>Alder Point, CA, 90417</p>
      <ul class="contact-list">
        <li>
          <svg class="contact-icon" viewBox="0 0 24 24" aria-hidden="true"><path d="M6.6 10.8a15.1 15.1 0 0 0 6.6 6.6l2.2-2.2a1 1 0 0 1 1-.25 11.4 11.4 0 0 0 3.6.57 1 1 0 0 1 1 1V20a1 1 0 0 1-1 1A17 17 0 0 1 3 4a1 1 0 0 1 1-1h3.5a1 1 0 0 1 1 1c0 1.250.2 2.450.57 3.57a1 1 0 0 1-.25 1z" fill="var(--deep-red)"/></svg>
          <span>(T) 855-PEPA-RUV (855-737-2788)</span>
        </li>
        <li>
          <svg class="contact-icon" viewBox="0 0 24 24" aria-hidden="true"><path d="M6.6 10.8a15.1 15.1 0 0 0 6.6 6.6l2.2-2.2a1 1 0 0 1 1-.25 11.4 11.4 0 0 0 3.6.57 1 1 0 0 1 1 1V20a1 1 0 0 1-1 1A17 17 0 0 1 3 4a1 1 0 0 1 1-1h3.5a1 1 0 0 1 1 1c0 1.250.2 2.450.57 3.57a1 1 0 0 1-.25 1z" fill="var(--deep-red)"/></svg>
          <span>949-555-0142</span>
        </li>
        <li>
          <svg class="contact-icon" viewBox="0 0 24 24" aria-hidden="true"><rect x="6" y="2" width="12" height="20" rx="2" fill="var(--deep-red)"/><rect x="8" y="5" width="8" height="11" fill="#fff"/><circle cx="12" cy="19" r="1.2" fill="#fff"/></svg>
          <span>949.555.0187</span>
        </li>
        <li>
          <svg class="contact-icon" viewBox="0 0 24 24" aria-hidden="true"><circle cx="12" cy="12" r="10" fill="none" stroke="var(--deep-red)" stroke-width="2.4"/><circle cx="12" cy="12" r="4" fill="none" stroke="var(--deep-red)" stroke-width="2.4"/></svg>
          <span>howard@CharredRelish.com</span>
        </li>
      </ul>
    </div>
  </article>
</body>
</html>
```